Animal Eye Clinic needs a Business card

We are a new veterinary ophthalmology practice (Tessaly Animal Eye Care) and we need a business card designed. We only see animal eyes - we are not a regular veterinary clinic. We already have a logo. We are looking for a professional, good looking business card to hand out to our clients. We are looking for something simple but professional and contemporary. Our logo is likely the only picture/graphic that needs to be on the card.
Updates

Contact Information for Business Card

Marisol Dunkley, BSc, DVM, MSc, DipACVO
Veterinary Ophthalmologist

Phone: 250.418.3097
Email: tessalyanimaleyecare@mailbrook.net
Website: tessalyanimaleyecare.net
Address: 1840 Pellworth Rd
Kelowna, BC, V4T 8M3

Colors

Designer to choose colors to be used in the design.

Requirements
Must have
• Our logo (attached)

```html
<!DOCTYPE html>
<html lang="en">
<head>
<meta charset="utf-8">
<title>Marisol Dunkley – Tessaly Animal Eye Care</title>
<link rel="stylesheet" href="https://fonts.googleapis.com/css2?family=Nanum+Gothic:wght@400;700&display=swap">
<style>
  :root {
    --teal: #2fc4ab;
    --ink: #2b2b2b;
    --paper: #ffffff;
    --disc: #efefef;
    --disc-text: #e2e2e2;
  }
  html, body {
    margin: 0;
    padding: 0;
    overflow: hidden;
    background: var(--paper);
  }
  .card {
    position: relative;
    width: 1200px;
    height: 667px;
    background: var(--paper);
    overflow: hidden;
    font-family: "Nanum Gothic", sans-serif;
    color: var(--ink);
  }
  .brand-disc {
    position: absolute;
    left: 710px;
    top: -1px;
    width: 860px;
    height: 860px;
    border-radius: 50%;
    background: var(--disc);
  }
  .brand-name {
    position: absolute;
    left: 935px;
    top: 500px;
    margin: 0;
    font-size: 40px;
    font-weight: 700;
    line-height: 1.1;
    color: var(--disc-text);
  }
  .identity {
    position: absolute;
    left: 0;
    width: 1200px;
    top: 186px;
    text-align: center;
  }
  .person-name {
    margin: 0;
    font-size: 33px;
    font-weight: 700;
    color: var(--teal);
    letter-spacing: 0.2px;
  }
  .person-role {
    margin: 10px 0 0;
    font-size: 32px;
    font-weight: 400;
    color: var(--ink);
  }
  .divider {
    position: absolute;
    left: 289px;
    top: 318px;
    width: 634px;
    height: 1px;
    background: var(--teal);
  }
  .contacts {
    position: absolute;
    left: 370px;
    top: 354px;
    margin: 0;
    padding: 0;
    list-style: none;
  }
  .contacts li {
    display: flex;
    align-items: center;
    height: 32.5px;
    font-size: 23px;
    color: var(--ink);
  }
  .contacts svg {
    width: 22px;
    height: 22px;
    margin-right: 54px;
    fill: none;
    stroke: var(--ink);
    stroke-width: 1.3;
  }
</style>
</head>
<body>
<main class="card">
  <div class="brand-disc"></div>
  <p class="brand-name">Tessaly<br>Animal<br>Eye Care</p>

  <header class="identity">
    <h1 class="person-name">Marisol Dunkley, BSc, DVM, MSc, DipACVO</h1>
    <p class="person-role">Veterinary Ophthalmologist</p>
  </header>

  <div class="divider"></div>

  <ul class="contacts">
    <li>
      <svg viewBox="0 0 22 22" aria-hidden="true"><rect x="6" y="3" width="10" height="17" rx="1"/><line x1="8" y1="6" x2="14" y2="6"/><line x1="10" y1="17" x2="12" y2="17"/></svg>
      250.418.3097
    </li>
    <li>
      <svg viewBox="0 0 22 22" aria-hidden="true"><path d="M20 3 L2 11 L9 13 L11 20 Z"/><line x1="9" y1="13" x2="20" y2="3"/></svg>
      tessalyanimaleyecare@mailbrook.net
    </li>
    <li>
      <svg viewBox="0 0 22 22" aria-hidden="true"><rect x="1" y="6" width="17" height="7" rx="1"/><path d="M13 10 L13 20 L15.5 17.5 L18 21 L19.5 20 L17 16.5 L20 16 Z"/></svg>
      tessalyanimaleyecare.net
    </li>
    <li>
      <svg viewBox="0 0 22 22" aria-hidden="true"><path d="M11 19 C6 13 5 11 5 8.5 A6 6 0 0 1 17 8.5 C17 11 16 13 11 19 Z"/><circle cx="11" cy="8.5" r="2.3"/><path d="M4 20 H18"/></svg>
      1840 Pellworth Rd Kelowna, BC, V4T 8M3
    </li>
  </ul>
</main>
</body>
</html>
```